Gerald Fenwick for Police Juror

political-police juror-
We want the picture on the front of the card; the write up on the back of postcard with vertical line separating mailing address from wording
I want to approve it before were finished

Industry/Entity Type

Political

```html
<!DOCTYPE html>
<html lang="en">
<head>
<meta charset="utf-8">
<title>Gerald Fenwick for Police Juror – Postcard</title>
<link href="https://fonts.googleapis.com/css2?family=Oswald:wght@500;700&family=Open+Sans:wght@400;600;700;800&display=swap" rel="stylesheet">
<style>
  :root {
    --page: #ffffff;
    --card: #ffffff;
    --ink: #2b2b2b;
    --ink-soft: #4a4a4a;
    --red: #d7262b;
    --goal-bg: #f1f1f1;
    --photo-dark: #16181c;
    --photo-mid: #3a3d44;
    --photo-light: #d9dadc;
    --shadow: rgba(0,0,0,0.18);
  }
  * { box-sizing: border-box; margin: 0; padding: 0; }
  html, body { width: 900px; height: 1200px; overflow: hidden; background: var(--page); }
  body { position: relative; font-family: "Open Sans", Arial, sans-serif; color: var(--ink); }

  .postcard {
    position: absolute;
    left: 45px;
    width: 825px;
    height: 570px;
    background: var(--card);
    box-shadow: 0 4px 14px var(--shadow);
    overflow: hidden;
  }
  .postcard--front { top: 18px; }
  .postcard--back { top: 612px; }

  /* Front */
  .front-photo {
    position: absolute;
    left: 0; top: 0;
    width: 390px; height: 100%;
    background: linear-gradient(90deg, var(--photo-light) 0%, var(--photo-mid) 22%, var(--photo-dark) 50%, var(--photo-mid) 80%, var(--photo-light) 100%);
  }
  .front-copy {
    position: absolute;
    left: 405px; top: 100px; right: 30px;
  }
  .front-tagline {
    font-family: "Open Sans", Arial, sans-serif;
    font-weight: 800;
    font-size: 21px;
    color: var(--ink);
    margin-bottom: 8px;
  }
  .front-headline {
    font-family: "Oswald", "Arial Narrow", sans-serif;
    font-weight: 700;
    text-transform: uppercase;
    line-height: 1;
    color: var(--ink);
  }
  .front-headline .why {
    display: block;
    color: var(--red);
    font-size: 118px;
    letter-spacing: 2px;
    line-height: 1;
  }
  .front-headline .rest {
    display: block;
    font-size: 47px;
    line-height: 1.12;
    margin-top: 2px;
  }
  .front-address {
    position: absolute;
    left: 560px; top: 455px;
    font-size: 16px;
    line-height: 1.45;
    color: var(--ink-soft);
  }

  /* Back */
  .back-intro {
    position: absolute;
    left: 42px; top: 50px;
    width: 560px;
    font-size: 16.5px;
    line-height: 1.5;
    color: var(--ink-soft);
  }
  .back-intro p + p { margin-top: 14px; }
  .back-intro strong { color: var(--red); font-weight: 700; }
  .stamp-box {
    position: absolute;
    left: 645px; top: 40px;
    width: 130px; height: 118px;
    border: 2px solid var(--ink);
  }
  .goal-box {
    position: absolute;
    left: 42px; top: 268px;
    width: 575px; height: 282px;
    background: var(--goal-bg);
    border: 2px solid var(--red);
    padding: 14px 18px;
  }
  .goal-lead {
    color: var(--red);
    font-weight: 700;
    font-size: 14.5px;
    line-height: 1.4;
    margin-bottom: 8px;
  }
  .goal-list { list-style: none; }
  .goal-list li {
    position: relative;
    padding-left: 16px;
    font-size: 13px;
    line-height: 1.38;
    color: var(--ink-soft);
    margin-bottom: 4px;
  }
  .goal-list li::before {
    content: "";
    position: absolute;
    left: 2px; top: 6px;
    width: 6px; height: 6px;
    border-radius: 50%;
    background: var(--red);
  }
</style>
</head>
<body>

  <section class="postcard postcard--front">
    <div class="front-photo" role="img" aria-label="Photo of a uniformed police officer seen from behind, hands clasped at the back"></div>
    <div class="front-copy">
      <p class="front-tagline">Gerald Fenwick for Police Juror</p>
      <h1 class="front-headline">
        <span class="why">Why</span>
        <span class="rest">Am I running<br>for District<br>3 Police<br>Juror?</span>
      </h1>
    </div>
    <address class="front-address" style="font-style: normal;">
      Gerry Fenwick<br>
      317 Harlow Bend Loop<br>
      Pinebrook, LA 70999
    </address>
  </section>

  <section class="postcard postcard--back">
    <div class="back-intro">
      <p>I am <strong>Gerald (Gerry) Fenwick</strong>, and I have been a resident of Cedar Parish for 36 years. I am married to Diane Marsh Fenwick, and together we have 8 children/stepchildren.</p>
      <p>I have owned and operated successful businesses for the past 21 years, including management positions in the oil industry, as well as designed and built state highways, parish roads, and city streets.</p>
    </div>
    <div class="stamp-box" aria-label="Stamp area"></div>
    <div class="goal-box">
      <p class="goal-lead">My goals as your next Police Juror will be to serve our parish as a FULL TIME JUROR, working along with fellow jurors, doing what is right for the people and the parish.</p>
      <ul class="goal-list">
        <li>Work proactively on projects and budgeting insuring our money is spent effectively and efficiently</li>
        <li>Hold contractors and employees accountable for providing quality goods and services</li>
        <li>Insure all roadways and bridges are safe and maintained properly</li>
        <li>Search and apply for available grants that will add additional revenue</li>
        <li>Start a committee of community leaders to discuss how best to make improvements to our district</li>
      </ul>
    </div>
  </section>

</body>
</html>
```